Create a banner for a Gmail email signature

We need a graphic design to use in a solicitor's email signature. The banner will incorporate a head shot of the solicitor as well as the law firm's logo and contact details. The solicitor's photo and law firm's logo are uploaded in the task.

```html
<!DOCTYPE html>
<html lang="en">
<head>
<meta charset="utf-8">
<title>Email Signature Banners</title>
<link rel="stylesheet" href="https://fonts.googleapis.com/css2?family=Arimo&family=Open+Sans:wght@400&family=Encode+Sans+Condensed:wght@400&display=swap">
<style>
  :root {
    --page: #f4f4f7;
    --halo: #ebe4f3;
    --card: #ffffff;
    --lilac: #bb9aca;
    --blue: #86a6cb;
    --plum: #8e4585;
    --ink: #111111;
    --photo-light: #e6cfa9;
    --photo-dark: #2e3a5c;
  }
  * { margin: 0; padding: 0; box-sizing: border-box; }
  html, body {
    width: 1200px;
    height: 1131px;
    overflow: hidden;
    background: var(--page);
  }
  .canvas {
    position: relative;
    width: 1200px;
    height: 1131px;
  }
  .banner-stage {
    position: absolute;
    left: 0;
    width: 1192px;
    height: 207px;
    background: var(--halo);
    box-shadow: 0 0 24px 10px var(--halo);
  }
  .banner-stage--lilac { top: 124px; }
  .banner-stage--blue { top: 470px; }

  .signature {
    position: absolute;
    left: 77px;
    top: 24px;
    width: 1038px;
    height: 159px;
    background: var(--card);
  }
  .signature__wave {
    position: absolute;
    left: 0;
    top: 0;
    width: 1038px;
    height: 159px;
  }
  .signature__contact {
    position: absolute;
    left: 98px;
    top: 22px;
    font-family: "Arimo", Arial, sans-serif;
    color: var(--ink);
  }
  .contact__name {
    font-size: 33px;
    letter-spacing: 3px;
    line-height: 36px;
  }
  .contact__line {
    font-size: 16px;
    letter-spacing: 2.4px;
    line-height: 18px;
    margin-left: 23px;
  }
  .signature__divider {
    position: absolute;
    top: 14px;
    width: 2px;
    height: 116px;
    background: var(--lilac);
  }
  .signature__divider--left { left: 417px; }
  .signature__divider--right { left: 577px; }
  .signature__portrait {
    position: absolute;
    left: 444px;
    top: 23px;
    width: 111px;
    height: 102px;
    background: linear-gradient(135deg, #8d95a6 0%, var(--photo-light) 40%, #d9c4b4 60%, var(--photo-dark) 100%);
  }
  .signature__brand {
    position: absolute;
    left: 599px;
    top: 44px;
    width: 404px;
    text-align: right;
  }
  .brand__name {
    display: flex;
    align-items: center;
    justify-content: flex-end;
    gap: 10px;
    font-family: "Open Sans", Arial, sans-serif;
    font-weight: 400;
    font-size: 40px;
    line-height: 48px;
    color: var(--plum);
    letter-spacing: -0.5px;
  }
  .brand__dot {
    width: 18px;
    height: 18px;
    border-radius: 50%;
    background: var(--plum);
    flex: none;
  }
  .brand__tagline {
    font-family: "Encode Sans Condensed", "Arial Narrow", sans-serif;
    font-size: 17px;
    line-height: 20px;
    color: var(--ink);
    margin-top: 12px;
    margin-right: -1px;
  }
</style>
</head>
<body>
<main class="canvas">

  <section class="banner-stage banner-stage--lilac">
    <article class="signature">
      <svg class="signature__wave" viewBox="0 0 1038 159" aria-hidden="true">
        <path fill="var(--lilac)" d="M0,6 Q0,0 6,0 Q11,0 12,4 L22,55 C27,80 37,95 55,103 C70,108 90,109 110,109 L366,109 C378,109 386,116 391,125 C396,136 404,147 418,147 L1032,147 A5.5,5.5 0 0 1 1032,158 L0,158 Z"/>
      </svg>
      <div class="signature__contact">
        <p class="contact__name">Lorem ipsum</p>
        <p class="contact__line">T-024-987-310-5</p>
        <p class="contact__line">@-dolor Amets</p>
      </div>
      <span class="signature__divider signature__divider--left"></span>
      <div class="signature__portrait" role="img" aria-label="Head shot of the solicitor"></div>
      <span class="signature__divider signature__divider--right"></span>
      <div class="signature__brand">
        <p class="brand__name"><span class="brand__dot"></span>KINSLEY LANE LAW</p>
        <p class="brand__tagline">Solicitors-North Shore</p>
      </div>
    </article>
  </section>

  <section class="banner-stage banner-stage--blue">
    <article class="signature">
      <svg class="signature__wave" viewBox="0 0 1038 159" aria-hidden="true">
        <path fill="var(--blue)" d="M0,6 Q0,0 6,0 Q11,0 12,4 L22,55 C27,80 37,95 55,103 C70,108 90,109 110,109 L366,109 C378,109 386,116 391,125 C396,136 404,147 418,147 L1032,147 A5.5,5.5 0 0 1 1032,158 L0,158 Z"/>
        <path fill="var(--lilac)" d="M0,78 L11,101 Q13,106 8,108 L0,111 Z"/>
      </svg>
      <div class="signature__contact">
        <p class="contact__name">Lorem ipsum</p>
        <p class="contact__line">T-024-987-310-5</p>
        <p class="contact__line">@-dolor Amets</p>
      </div>
      <span class="signature__divider signature__divider--left"></span>
      <div class="signature__portrait" role="img" aria-label="Head shot of the solicitor"></div>
      <span class="signature__divider signature__divider--right"></span>
      <div class="signature__brand">
        <p class="brand__name"><span class="brand__dot"></span>KINSLEY LANE LAW</p>
        <p class="brand__tagline">Solicitors-North Shore</p>
      </div>
    </article>
  </section>

</main>
</body>
</html>
```